Android Shop Depot Listing Screenshot Design

We would like to create new screenshots for our Android app in the Shop Depot to A/B test against the current version.

You can view our current Android Shop Depot listing here: https://shop.trelvani.com/store/apps/details?id=com.quorvix.android&hl=en

Attached I have added screenshots of the app that I would like to be included. Please edit the screenshots to generic text (e.g. John Smith, 123 Main St, etc.).

You can use the same text we have in the current ones. For text for the criminal screenshot please view our iOS Kiosk Hub listing: https://apps.mondrelo.com/us/app/quorvix-background-check/id918274650?mt=8

If you want to come up with new text please feel free to!

I also attached a few examples of other app screenshots that we like.

Android ShopDepot Listing Guidelines: https://help.trelvani.com/trelvanishop/android-developer/answer/5520931?hl=en

Industry/Entity Type

Store

Font styles to use
Sans Serif

Colors
f0f0f0

Requirements
Must have
• ~Generic names and data like "John Smith", "54 Main St. Springfield, NJ 09876"
• ~Screenshot for Person Search, Criminal Records, Phone Search, Email Search, and Property Search. In that order.
• ~Headlines either the ones used in our current screenshots (https://shop.trelvani.com/store/apps/details?id=com.quorvix.android&hl=en) or new ones you come up with.
• ~Must meet Android screenshot guidelines.
• ~Optimized for downloads.
• Must use following color palette:
• Dark purple #3B2469
• Light purple #7E6F9C
• Very dark gray #333333
• Dark gray #666666
• Gray #999999
• Blue gray #CFD9DE
• Green #5CB85C
• Navy #003577
• Yellow #F3B607
• Magenta #F0386B

```html
<!DOCTYPE html>
<html lang="en">
<head>
<meta charset="utf-8">
<title>Search by Email</title>
<link rel="stylesheet" href="https://fonts.googleapis.com/css2?family=Roboto:wght@300;400;500;700&display=swap">
<style>
:root{
  --dark-purple:#3B2469;
  --bar-purple:#462d74;
  --light-purple:#7E6F9C;
  --ink:#333333;
  --ink-soft:#666666;
  --gray:#999999;
  --blue-gray:#CFD9DE;
  --green:#5CB85C;
  --link:#3a7bd5;
  --device:#1f1f1f;
  --white:#ffffff;
}
*{margin:0;padding:0;box-sizing:border-box}
html,body{width:675px;height:1200px;overflow:hidden}
body{font-family:"Roboto",Arial,sans-serif;background:var(--blue-gray);position:relative}
.band{position:absolute;inset:0}
.band-purple{background:var(--light-purple);clip-path:polygon(0 380px,675px 516px,675px 1200px,0 1200px)}
.band-green{background:var(--green);clip-path:polygon(0 1022px,675px 858px,675px 1200px,0 1200px)}

.headline{position:absolute;left:74px;top:51px;display:flex;align-items:center}
.headline-badge{width:124px;height:124px;border-radius:50%;background:var(--dark-purple)}
.headline-text{margin-left:28px;color:var(--ink);line-height:1}
.headline-text .lead{display:block;font-size:53px;font-weight:500;letter-spacing:.5px}
.headline-text .key{display:block;font-size:66px;font-weight:700;margin-top:6px}

.device{position:absolute;left:70px;top:283px;width:544px;height:1000px;border-radius:56px;background:var(--device)}
.device-speaker{position:absolute;left:174px;top:38px;width:197px;height:16px;border-radius:8px;background:#3a3a3a}
.device-camera{position:absolute;left:93px;top:35px;width:18px;height:18px;border-radius:50%;background:#333;border:3px solid #161616}

.screen{position:absolute;left:96px;top:392px;width:493px;height:808px;background:var(--white);overflow:hidden}
.status-bar{height:33px;background:var(--dark-purple);display:flex;align-items:center;padding:0 14px;color:var(--white);font-size:17px}
.status-bar .left{display:flex;gap:12px}
.status-bar .right{margin-left:auto;display:flex;align-items:center;gap:10px}
.status-bar .time{font-size:22px}
.app-bar{height:77px;background:var(--bar-purple);position:relative;color:var(--white)}
.app-bar .title{position:absolute;left:98px;top:22px;font-size:27px;font-weight:500}
.app-bar svg{position:absolute}

.report-header{position:absolute;left:0;top:110px;width:493px;height:203px;background:linear-gradient(90deg,#7a6e9f,#6d639c);clip-path:polygon(0 0,493px 0,493px 159px,0 203px)}
.report-email{position:absolute;left:0;top:127px;width:493px;text-align:center;color:var(--white);font-size:27px;font-weight:300}
.owner-photo{position:absolute;left:164px;top:177px;width:166px;height:166px;border-radius:50%;border:3px solid var(--white);background:radial-gradient(circle at 50% 45%,#c9a58a,#6f8a6a 70%,#9fb7c4)}

.section-title{position:absolute;left:8px;font-size:35.5px;font-weight:400;color:var(--dark-purple);white-space:nowrap}
.overview-title{top:362px}
.field-label{position:absolute;left:8px;top:421px;font-size:21.5px;font-weight:500;color:var(--gray)}
.field-value{position:absolute;left:8px;top:456px;font-size:23px;color:var(--ink)}
.divider-thick{position:absolute;left:0;top:499px;width:493px;height:4px;background:#ececec}
.social-title{top:511px}
.help-dot{position:absolute;left:449px;top:518px}

.site-row{position:absolute;left:0;width:493px;height:89px}
.site-icon{position:absolute;left:19px;top:18px;width:52px;height:52px;border-radius:50%}
.site-name{position:absolute;left:96px;top:8px;font-size:21px;color:var(--ink)}
.site-url{position:absolute;left:96px;top:42px;font-size:19px;color:var(--link)}
.row-divider{position:absolute;left:8px;bottom:0;width:478px;height:1px;background:#e3e3e3}
.icon-sky{background:#2fa5e3}
.icon-royal{background:#3b5a99}
.icon-deep{background:#0f6fab}
.fab{position:absolute;left:395px;top:779px;width:78px;height:78px;border-radius:50%;background:var(--green)}
</style>
</head>
<body>
<div class="band band-purple"></div>
<div class="band band-green"></div>

<header class="headline">
  <div class="headline-badge"></div>
  <h1 class="headline-text"><span class="lead">Search by</span><span class="key">Email</span></h1>
</header>

<div class="device">
  <div class="device-speaker"></div>
  <div class="device-camera"></div>
</div>

<main class="screen">
  <div class="status-bar">
    <div class="left">
      <svg width="18" height="16" aria-hidden="true"><rect x="1" y="1" width="16" height="14" fill="none" stroke="#fff" stroke-width="2"/></svg>
      <svg width="18" height="16" aria-hidden="true"><rect x="1" y="2" width="16" height="12" fill="#fff"/><polyline points="1,2 9,9 17,2" fill="none" stroke="#3B2469" stroke-width="2"/></svg>
      <svg width="14" height="16" aria-hidden="true"><rect x="1" y="1" width="12" height="14" fill="#fff"/></svg>
    </div>
    <div class="right">
      <svg width="20" height="18" aria-hidden="true"><path d="M2 6h4l5-4v14l-5-4H2z" fill="#fff"/><line x1="1" y1="1" x2="19" y2="17" stroke="#fff" stroke-width="2"/></svg>
      <svg width="22" height="18" aria-hidden="true"><path d="M1 6a14 14 0 0 1 20 0M4 10a9 9 0 0 1 14 0M8 14a4 4 0 0 1 6 0" fill="none" stroke="#fff" stroke-width="2"/></svg>
      <svg width="20" height="18" aria-hidden="true"><polygon points="1,17 19,1 19,17" fill="#9a8fb8"/></svg>
      <span>18%</span>
      <svg width="12" height="20" aria-hidden="true"><rect x="1" y="2" width="10" height="17" fill="none" stroke="#fff" stroke-width="1.5"/><rect x="2" y="15" width="8" height="4" fill="#fff"/></svg>
      <span class="time">5:11 PM</span>
    </div>
  </div>
  <nav class="app-bar">
    <svg style="left:28px;top:28px" width="24" height="22" aria-hidden="true"><path d="M22 11H3M11 2 2 11l9 9" fill="none" stroke="#fff" stroke-width="2.5"/></svg>
    <span class="title">Email Report</span>
    <svg style="left:378px;top:22px" width="32" height="34" aria-hidden="true"><path d="M6 25V15a10 10 0 0 1 20 0v10l3 3H3z" fill="none" stroke="#fff" stroke-width="2.5"/><path d="M12 30a4 4 0 0 0 8 0" fill="#fff"/><path d="M16 10v10M11 15h10" stroke="#fff" stroke-width="2.5"/></svg>
    <svg style="left:446px;top:24px" width="30" height="30" aria-hidden="true"><circle cx="15" cy="15" r="13" fill="none" stroke="#fff" stroke-width="2.5"/><path d="M11 12a4 4 0 1 1 5 4v3" fill="none" stroke="#fff" stroke-width="2.5"/><circle cx="16" cy="23" r="1.6" fill="#fff"/></svg>
  </nav>

  <div class="report-header"></div>
  <p class="report-email">johndoe@postvale.net</p>
  <div class="owner-photo" role="img" aria-label="Portrait photo of the email owner"></div>

  <h2 class="section-title overview-title">Email Overview</h2>
  <p class="field-label">OWNER</p>
  <p class="field-value">JOHN DOE</p>
  <div class="divider-thick"></div>

  <h2 class="section-title social-title">Social Media &amp; Websites</h2>
  <svg class="help-dot" width="34" height="34" aria-hidden="true"><circle cx="17" cy="17" r="15" fill="none" stroke="#999" stroke-width="2.5"/><path d="M13 14a4 4 0 1 1 5 4v3" fill="none" stroke="#999" stroke-width="2.5"/><circle cx="18" cy="25" r="1.6" fill="#999"/></svg>

  <div class="site-row" style="top:565px">
    <span class="site-icon icon-sky"></span>
    <span class="site-name">Birdcall</span>
    <span class="site-url">https://birdcall.net/JohnDoe</span>
    <span class="row-divider"></span>
  </div>
  <div class="site-row" style="top:654px">
    <span class="site-icon icon-royal"></span>
    <span class="site-name">Friendspace</span>
    <span class="site-url">https://friendspace.net/JohnDoe</span>
    <span class="row-divider"></span>
  </div>
  <div class="site-row" style="top:743px">
    <span class="site-icon icon-deep"></span>
    <span class="site-name">Workhub</span>
    <span class="site-url">https://workhub.net/JohnDoe</span>
  </div>
  <div class="fab"></div>
</main>
</body>
</html>
```